Logo needed for business card

Velquist Pty Ltd is in the business of healthcare and ecommerce.

We own and manage pharmacies and online health ecomerce sites.

We provide ecommerce consultants for companies looking for an ecommerce business startegy.

Think of it as the umbrella under which several healthcare brands may sit.

When I think of Velquist, I visulaise slick black/metalic colours, so please stay away from the common blue and green colours that seem to be so popular in this field.

Target Market(s)

CEOs and COOs

Industry/Entity Type

Healthcare

Contact Information for Business Card

Tessa Lindqvist
Director
Velquist Pty Ltd
4/362 Fennick Pde
Brellton, NSW 2148

Requirements
Must have
• Design must have scope to be implemented on the company's website and letterheads etc.

```html
<!DOCTYPE html>
<html lang="en">
<head>
<meta charset="utf-8">
<title>Velquist Pty Ltd – Business Card</title>
<link rel="stylesheet" href="https://fonts.googleapis.com/css2?family=Oswald:wght@600&family=Open+Sans:wght@400&display=swap">
<style>
  :root {
    --page: #ffffff;
    --card: #2d2f31;
    --band: #1f2021;
    --side-block: #6d7073;
    --ghost: #393b3d;
    --white: #ffffff;
    --accent: #0aa6c8;
    --mark-ring: #ffffff;
    --mark-fill: #8d9093;
  }
  html, body {
    margin: 0;
    padding: 0;
    width: 1200px;
    height: 1000px;
    overflow: hidden;
    background: var(--page);
  }
  .canvas {
    position: relative;
    width: 1200px;
    height: 1000px;
  }
  .card {
    position: absolute;
    left: 62px;
    top: 196px;
    width: 1076px;
    height: 606px;
    background: var(--card);
    overflow: hidden;
  }
  .ghost-name {
    position: absolute;
    margin: 0;
    font-family: "Oswald", "Arial Narrow", sans-serif;
    font-weight: 600;
    color: var(--ghost);
    white-space: nowrap;
    line-height: 1;
    letter-spacing: -1px;
  }
  .ghost-name--top {
    left: 336px;
    top: -12px;
    font-size: 100px;
  }
  .ghost-name--bottom {
    left: 82px;
    top: 478px;
    font-size: 118px;
  }
  .info-band {
    position: absolute;
    left: 0;
    top: 192px;
    width: 1076px;
    height: 222px;
    background: var(--band);
  }
  .info-band__block {
    position: absolute;
    left: 0;
    top: 0;
    width: 108px;
    height: 222px;
    background: var(--side-block);
  }
  .person {
    position: absolute;
    left: 136px;
    top: 4px;
  }
  .person__name {
    margin: 0;
    font-family: "Oswald", "Arial Narrow", sans-serif;
    font-weight: 600;
    font-size: 42px;
    line-height: 1.1;
    color: var(--white);
    letter-spacing: -0.5px;
  }
  .person__first { color: var(--accent); }
  .person__role {
    margin: 0;
    font-family: "Open Sans", Arial, sans-serif;
    font-size: 25px;
    line-height: 1;
    color: var(--white);
  }
  .address {
    position: absolute;
    left: 129px;
    top: 185px;
    margin: 0;
    font-family: "Open Sans", Arial, sans-serif;
    font-size: 25px;
    color: var(--white);
    white-space: nowrap;
  }
  .brand-mark {
    position: absolute;
    left: 868px;
    top: 30px;
    width: 168px;
    height: 160px;
    display: flex;
    flex-direction: column;
    align-items: center;
    justify-content: center;
    gap: 10px;
  }
  .brand-mark__name {
    font-family: "Oswald", "Arial Narrow", sans-serif;
    font-weight: 600;
    font-size: 30px;
    color: var(--white);
    line-height: 1;
  }
  .wordmark {
    position: absolute;
    left: 640px;
    top: 446px;
    margin: 0;
    font-family: "Oswald", "Arial Narrow", sans-serif;
    font-weight: 600;
    font-size: 44px;
    line-height: 1;
    color: var(--white);
    white-space: nowrap;
  }
</style>
</head>
<body>
<div class="canvas">
  <section class="card" aria-label="Velquist Pty Ltd business card">
    <p class="ghost-name ghost-name--top" aria-hidden="true">VELQUIST Pty Ltd</p>
    <p class="ghost-name ghost-name--bottom" aria-hidden="true">VELQUIST Pty Ltd</p>

    <div class="info-band">
      <div class="info-band__block"></div>
      <div class="person">
        <h1 class="person__name"><span class="person__first">Tessa</span> Lindqvist</h1>
        <p class="person__role">Director</p>
      </div>
      <p class="address">Velquist Pty Ltd 4/362 Fennick Pde Brellton, NSW 2148</p>

      <div class="brand-mark">
        <svg width="60" height="60" viewBox="0 0 60 60" aria-hidden="true">
          <circle cx="30" cy="30" r="27" fill="var(--mark-fill)" stroke="var(--mark-ring)" stroke-width="4"/>
        </svg>
        <span class="brand-mark__name">VELQUIST</span>
      </div>
    </div>

    <p class="wordmark">VELQUIST Pty Ltd</p>
  </section>
</div>
</body>
</html>
```